Clinic for cellulit and fat removal

Name of clinic :
Lumera
- Body & Health (this has to be written on the site.)
I need CMS for me to be able to make changes myself.
A webpage for woman searching for a solution to remove fat and cellulit.
The owner is a brazilian woman in Denmark, and want her sense of aestetic shines thru the website.
There needs to be a slide show on the landing page showing big sliding pictures, of the clinic and and the treatments.
The Cryolipolysis, is a treatment freezing fat and cellulit, and this treatment will be the Attraction of the clinic.
Needs These pages in a horisontal fasion. (written in Danish)
Lumera
Behandlinger
- Cryolipolysis
- Silkora
- Lymfemassage
- Tandrelia
- Copper Tide
Produkter
Priser
Kontakt

```html
<!DOCTYPE html>
<html lang="da">
<head>
<meta charset="utf-8">
<title>Lumera – Produkter</title>
<link rel="stylesheet" href="https://fonts.googleapis.com/css2?family=Open+Sans:wght@400;600&family=Pacifico&display=swap">
<style>
  :root {
    --mint: #7fd3b4;
    --mint-soft: #dcfbef;
    --mint-hover: #eefaf5;
    --magenta: #b83a8c;
    --ink: #1f1f1f;
    --muted: #8a8f8c;
    --line: #c9ece0;
    --page: #fbfbfb;
    --card: #ffffff;
    --product-bg: #f7f7f7;
    --skin-light: #f1dccb;
    --skin-deep: #c98e6a;
  }
  * { box-sizing: border-box; margin: 0; padding: 0; }
  html, body { width: 1200px; height: 675px; overflow: hidden; }
  body {
    position: relative;
    background: var(--page);
    font-family: "Open Sans", Arial, sans-serif;
    color: var(--ink);
  }

  /* Sidebar */
  .sidebar {
    position: absolute; left: 0; top: 0;
    width: 200px; height: 675px;
    background: #fff;
    box-shadow: 1px 0 6px rgba(0,0,0,0.04);
    z-index: 2;
  }
  .brand { position: absolute; left: 38px; top: 34px; }
  .brand-name {
    display: flex; align-items: center; gap: 8px;
    font-size: 28px; font-weight: 400; color: var(--ink); letter-spacing: 0.5px;
  }
  .brand-dot { width: 12px; height: 12px; border-radius: 50%; background: var(--mint); }
  .brand-tagline {
    margin-top: 2px; margin-left: 20px;
    font-size: 11px; font-weight: 600; color: var(--magenta); letter-spacing: 0.6px;
  }
  .main-nav { position: absolute; left: 0; top: 136px; width: 200px; list-style: none; }
  .main-nav li {
    height: 47px; line-height: 46px;
    padding-left: 30px;
    font-size: 10.5px; letter-spacing: 0.4px;
    border-top: 1px dotted var(--line);
  }
  .main-nav li:last-child { border-bottom: 1px dotted var(--line); }
  .main-nav li.is-active { background: var(--mint-soft); border-right: 2px solid var(--mint); }

  .social { position: absolute; left: 34px; top: 616px; display: flex; align-items: center; gap: 22px; }
  .social span { display: block; border-radius: 50%; }
  .social .social-main { width: 28px; height: 28px; background: var(--mint); }
  .social .social-small { width: 9px; height: 9px; border: 1.5px solid var(--mint); }

  /* Right-side body photo */
  .hero-photo {
    position: absolute; right: 0; top: 0;
    width: 150px; height: 675px;
    background: linear-gradient(100deg, rgba(241,220,203,0) 0%, var(--skin-light) 22%, #dcb091 55%, var(--skin-deep) 100%);
  }

  /* Content */
  .page-title {
    position: absolute; left: 200px; right: 0; top: 22px;
    text-align: center;
    font-family: "Pacifico", cursive;
    font-size: 40px; font-weight: 400;
    color: var(--magenta);
  }
  .products { position: absolute; left: 222px; top: 164px; display: flex; gap: 19px; }
  .product-card {
    width: 225px; height: 343px;
    background: var(--card);
    box-shadow: 0 1px 6px rgba(0,0,0,0.08);
    position: relative;
  }
  .product-image {
    height: 297px; background: var(--product-bg);
    display: flex; align-items: center; justify-content: center;
    border-bottom: 1px dotted var(--line);
  }
  .bottle-photo {
    width: 108px; height: 213px; margin-top: 8px;
    border-radius: 14px 14px 22px 22px;
    background: linear-gradient(90deg, #e6e6e6, #fdfdfd 45%, #dcdcdc);
  }
  .product-info {
    height: 46px; padding: 0 10px 0 11px;
    display: flex; align-items: center; justify-content: space-between;
    font-size: 10.5px; letter-spacing: 0.6px;
  }
  .product-price { color: var(--magenta); }

  .product-card.is-hover { background: var(--mint-hover); }
  .product-card.is-hover .product-image { background: var(--mint-hover); }
  .product-card.is-hover .bottle-photo { opacity: 0.65; }
  .product-card.is-hover .product-info { color: var(--muted); }
  .product-card.is-hover .product-price { color: #c47aab; }
  .card-actions {
    position: absolute; left: 0; right: 0; top: 155px;
    display: flex; justify-content: center; gap: 10px;
  }
  .card-action {
    width: 37px; height: 37px; border-radius: 50%;
    background: #fff;
    display: flex; align-items: center; justify-content: center;
  }

  .footer-note {
    position: absolute; right: 22px; top: 632px;
    font-size: 9px; color: var(--ink);
  }
</style>
</head>
<body>
  <aside class="sidebar">
    <div class="brand">
      <div class="brand-name"><span class="brand-dot"></span>Lumera</div>
      <div class="brand-tagline">Body &amp; Health</div>
    </div>
    <ul class="main-nav">
      <li>Lumera</li>
      <li>Behandlinger</li>
      <li class="is-active">Produkter</li>
      <li>Priser</li>
      <li>Kontakt</li>
    </ul>
    <div class="social" aria-label="Sociale medier">
      <span class="social-main"></span>
      <span class="social-small"></span>
      <span class="social-small"></span>
      <span class="social-small"></span>
    </div>
  </aside>

  <div class="hero-photo" role="img" aria-label="Photo of a woman's waist and hip in soft skin tones"></div>

  <h1 class="page-title">Produkter</h1>

  <section class="products">
    <article class="product-card">
      <div class="product-image"><div class="bottle-photo" role="img" aria-label="White supplement bottle with mint figure label"></div></div>
      <div class="product-info"><span>Lorem ipsum dolor</span><span class="product-price">€20.00</span></div>
    </article>
    <article class="product-card">
      <div class="product-image"><div class="bottle-photo" role="img" aria-label="White supplement bottle with mint figure label"></div></div>
      <div class="product-info"><span>Duis autem vel</span><span class="product-price">€20.00</span></div>
    </article>
    <article class="product-card is-hover">
      <div class="product-image"><div class="bottle-photo" role="img" aria-label="White supplement bottle with mint figure label"></div></div>
      <div class="card-actions">
        <span class="card-action" aria-label="Link">
          <svg width="14" height="14" viewBox="0 0 14 14" fill="none" stroke="#7fd3b4" stroke-width="1.6">
            <rect x="1.5" y="1.5" width="6" height="4" rx="2" transform="rotate(45 4.5 3.5)"/>
            <rect x="6.5" y="8.5" width="6" height="4" rx="2" transform="rotate(45 9.5 10.5)"/>
            <line x1="5" y1="5" x2="9" y2="9"/>
          </svg>
        </span>
        <span class="card-action" aria-label="Læg i kurv">
          <svg width="15" height="14" viewBox="0 0 15 14" fill="#7fd3b4">
            <path d="M0 1h2.5l.6 2H14l-1.4 5.5H4.3l.4 1.3h7.8v1.2H3.8L1.6 2.2H0z"/>
            <circle cx="5" cy="12.6" r="1.2"/><circle cx="11.2" cy="12.6" r="1.2"/>
          </svg>
        </span>
      </div>
      <div class="product-info"><span>Nam liber tempor</span><span class="product-price">€20.00</span></div>
    </article>
    <article class="product-card">
      <div class="product-image"><div class="bottle-photo" role="img" aria-label="White supplement bottle with mint figure label"></div></div>
      <div class="product-info"><span>Typi non habent</span><span class="product-price">€20.00</span></div>
    </article>
  </section>

  <p class="footer-note">© Copyright Lumera 2017</p>
</body>
</html>
```